Ferncrest Dental, LLC business card project

Business card to be designed with current logo.
Dental office- please keep design of card that looks clean and professional.
Please include the following info:
Ferncrest Dental, LLC
Dr. Lorna Pettigrew
2871 Marlowe Street
Ashbourne, OH 44093
740-555-0193
ferncrestdental.office@examplemail.test
Hello everyone-
Reason: Just got back from overseas- will look at all designs and provide feedback. Thank you!
Reason: Polling my friends for the final selection-
thank you to all those that participated- so many talented designers!

```html
<!DOCTYPE html>
<html lang="en">
<head>
<meta charset="utf-8">
<title>Ferncrest Dental, LLC – Business Card</title>
<link rel="stylesheet" href="https://fonts.googleapis.com/css2?family=Cormorant+Garamond:ital,wght@1,700&family=Crimson+Text:wght@400;600&display=swap">
<style>
  :root {
    --bg-light: #8aa6c9;
    --bg-mid: #5f86b5;
    --bg-dark: #174a8c;
    --band-light: #f4f4f4;
    --band-mid: #dcdcdc;
    --band-dark: #b9b9b9;
    --label-white: #ffffff;
    --brand-green: #5c9a37;
    --text-white: #ffffff;
    --panel-fill: rgba(30, 55, 95, 0.35);
    --panel-edge: rgba(200, 215, 235, 0.55);
  }
  * { margin: 0; padding: 0; box-sizing: border-box; }
  html, body {
    width: 1200px;
    height: 734px;
    overflow: hidden;
    background: var(--bg-dark);
  }
  .card {
    position: relative;
    width: 1200px;
    height: 734px;
    overflow: hidden;
    background: linear-gradient(90deg, var(--bg-light) 0%, var(--bg-mid) 30%, #3f6aa2 60%, var(--bg-dark) 100%);
  }
  .card-shapes {
    position: absolute;
    inset: 0;
  }
  .brand-label {
    position: absolute;
    left: 201px;
    top: 79px;
    width: 806px;
    height: 107px;
    display: flex;
    align-items: center;
    justify-content: center;
    gap: 18px;
  }
  .brand-dot {
    width: 26px;
    height: 26px;
    border-radius: 50%;
    background: var(--brand-green);
  }
  .brand-name {
    font-family: "Crimson Text", serif;
    font-weight: 600;
    font-size: 58px;
    line-height: 1;
    color: var(--brand-green);
    letter-spacing: 0.5px;
  }
  .doctor-name {
    position: absolute;
    left: 342px;
    width: 600px;
    top: 270px;
    text-align: center;
    font-family: "Cormorant Garamond", serif;
    font-style: italic;
    font-weight: 700;
    font-size: 48px;
    line-height: 1;
    color: var(--text-white);
  }
  .contact {
    position: absolute;
    left: 608px;
    top: 478px;
    font-family: "Crimson Text", serif;
    font-size: 30px;
    line-height: 38.5px;
    color: var(--text-white);
    list-style: none;
    white-space: nowrap;
  }
</style>
</head>
<body>
<main class="card">
  <svg class="card-shapes" width="1200" height="734" viewBox="0 0 1200 734" aria-hidden="true">
    <defs>
      <linearGradient id="band-fill" x1="0" y1="0" x2="0" y2="1">
        <stop offset="0" stop-color="var(--band-light)"/>
        <stop offset="0.6" stop-color="var(--band-mid)"/>
        <stop offset="1" stop-color="var(--band-dark)"/>
      </linearGradient>
      <linearGradient id="strap-fill" x1="0" y1="0" x2="1" y2="0">
        <stop offset="0" stop-color="#cfcfcf"/>
        <stop offset="0.5" stop-color="#f2f2f2"/>
        <stop offset="1" stop-color="#c4c4c4"/>
      </linearGradient>
    </defs>

    <!-- hanging straps -->
    <polygon class="strap-left" points="196,0 265,0 135,130 66,130" fill="url(#strap-fill)"/>
    <polygon class="strap-right" points="940,0 1006,0 1134,128 1068,128" fill="url(#strap-fill)"/>

    <!-- content panel -->
    <rect class="info-panel" x="65" y="196" width="1069" height="472" rx="6"
          fill="var(--panel-fill)" stroke="var(--panel-edge)" stroke-width="2"/>
    <rect x="71" y="200" width="1057" height="462" rx="4"
          fill="none" stroke="rgba(255,255,255,0.18)" stroke-width="1"/>

    <!-- header band -->
    <rect class="header-band" x="65" y="65" width="1069" height="135" rx="3" fill="url(#band-fill)"/>
    <polygon points="65,200 65,130 135,68 160,68 88,132 88,200" fill="#e9e9e9" opacity="0.7"/>
    <line x1="65" y1="200" x2="1134" y2="200" stroke="#8a8f96" stroke-width="2"/>

    <!-- label plate -->
    <rect class="label-plate" x="201" y="79" width="806" height="107" rx="6"
          fill="var(--band-mid)" stroke="#c2c2c2" stroke-width="2"/>
    <rect x="209" y="87" width="790" height="91" rx="3" fill="var(--label-white)" stroke="#d0d0d0"/>
  </svg>

  <div class="brand-label">
    <span class="brand-dot"></span>
    <span class="brand-name">Ferncrest Dental, LLC</span>
  </div>

  <h1 class="doctor-name">Dr. Lorna Pettigrew</h1>

  <ul class="contact">
    <li>Address: 2871 Marlowe Street</li>
    <li>Ashbourne, OH 44093</li>
    <li>Phone: 740-555-0193</li>
    <li>ferncrestdental.office@examplemail.test</li>
  </ul>
</main>
</body>
</html>
```